Broschüre für Anbieter von Haushaltshilfen und Alltagsbegleitern für Privathaushalte
Zielgruppe
Wir bieten Haushaltshilfen und Alltagsbegleiter für Privathaushalte an. Unsere Hauptkundenklientel sind Pflegebedürftige Menschen denen eine Haushaltshilfe von der Pflegekasse zusteht. Weitere Kunden sind Familien und/oder Singlehaushalte, die eine Haushaltfshilfe benötigen.
Aufgabenstellung
- Das Prospekt sollte DIN A4 sein, sind aber auch offen für andere Formate
- Farbdesign muß unsere Logofarben enthalten
- In dem Prospekt müßen unsere Leistungen wie auf unserer Internetseite www.lindaufeld.de beschrieben sein.
- Seitenanzahl insgesamt 4 Seiten

```html
<!DOCTYPE html>
<html lang="de">
<head>
<meta charset="utf-8">
<title>Lindaufeld – Broschüre</title>
<link rel="stylesheet" href="https://fonts.googleapis.com/css2?family=Open+Sans:wght@400;600;700;800&family=Caveat:wght@700&display=swap">
<style>
  :root{
    --red:#b3172a;
    --red-light:#e0505a;
    --red-deep:#8e1220;
    --ink:#1e1e20;
    --dark:#3a3a3c;
    --text:#555558;
    --paper:#f1f1f2;
    --backdrop:#d9d9db;
    --white:#ffffff;
  }
  *{box-sizing:border-box;margin:0;padding:0}
  html,body{width:1200px;height:856px;overflow:hidden}
  body{background:var(--backdrop);font-family:"Open Sans",Arial,sans-serif;color:var(--text)}
  .spread{position:absolute;left:34px;top:28px;width:1132px;height:800px;display:flex;box-shadow:0 6px 24px rgba(0,0,0,.18)}
  .page{position:relative;width:566px;height:800px;overflow:hidden;background:linear-gradient(180deg,#e6e6e8 0%,var(--paper) 35%,#fafafa 100%)}
  .page--left{border-right:1px solid #d0d0d2}

  .brand{position:absolute;left:34px;top:34px;display:flex;align-items:center;gap:12px}
  .brand__mark{width:34px;height:34px;border-radius:50%;background:var(--red)}
  .brand__name{font-family:"Open Sans",Arial,sans-serif;font-weight:700;font-size:26px;letter-spacing:1px;color:var(--dark)}
  .tagline{position:absolute;font-family:"Caveat",cursive;font-weight:700;font-size:26px;color:var(--red);transform:rotate(8deg)}
  .page--left .tagline{left:350px;top:30px}
  .page--right .tagline{left:370px;top:40px;transform:rotate(-10deg)}

  .headline{position:absolute;left:70px;top:108px;width:440px;font-weight:800;font-size:37px;line-height:1.15;color:var(--ink);text-align:center;text-transform:uppercase}
  .headline__swoosh{position:absolute;left:110px;top:196px}
  .intro{position:absolute;left:46px;top:232px;width:480px;text-align:center;font-size:16.5px;line-height:1.35;color:var(--text)}
  .intro strong{color:var(--red);font-weight:700}

  .photo{position:absolute;left:0;top:380px;width:566px;height:420px;background:radial-gradient(ellipse at 50% 40%,#e9d9cf 0%,#c9b6a8 35%,#9fb2c6 70%,#c8ccd2 100%)}
  .photo--faint{top:0;height:800px;background:radial-gradient(ellipse at 60% 45%,rgba(200,200,205,.55) 0%,rgba(225,225,228,.3) 45%,rgba(241,241,242,0) 75%)}

  .bands{position:absolute;left:0;top:0}
  .footer-url{position:absolute;left:0;width:566px;bottom:22px;text-align:center;color:var(--white);font-size:15px;letter-spacing:.5px}

  .ribbon{position:absolute;left:70px;top:100px}
  .benefits-intro{position:absolute;left:50px;top:196px;width:470px;font-size:10.5px;line-height:1.45;color:var(--text)}
  .benefit{position:absolute;display:flex;align-items:center;gap:14px;width:230px;font-size:10.5px;line-height:1.4;color:var(--text)}
  .benefit__icon{flex:none;width:52px;height:50px;border-radius:8px;background:var(--red);display:flex;align-items:center;justify-content:center}
  .benefit--billing{left:50px;top:288px}
  .benefit--amount{left:296px;top:268px;width:250px}
  .benefit--respite{left:50px;top:366px}
  .benefit--application{left:296px;top:330px;width:250px}

  .cta{position:absolute;left:0;width:566px;top:420px;text-align:center;font-weight:800;font-size:23px;color:var(--red)}
  .phone{position:absolute;left:118px;top:470px;display:flex;align-items:center}
  .phone__icon{width:46px;height:46px;border-radius:50%;border:3px solid var(--red);background:var(--white);display:flex;align-items:center;justify-content:center;position:relative;z-index:1}
  .phone__number{margin-left:-10px;background:var(--red);color:var(--white);font-weight:800;font-size:22px;letter-spacing:1px;padding:6px 26px 6px 32px;border-radius:0 12px 12px 0}
</style>
</head>
<body>
<main class="spread">

  <section class="page page--left">
    <div class="brand"><span class="brand__mark"></span><span class="brand__name">LINDAUFELD</span></div>
    <p class="tagline">Wir sind für Sie da!</p>

    <h1 class="headline">Verschenken Sie<br>nicht Ihr Geld!!</h1>
    <svg class="headline__swoosh" width="340" height="40" viewBox="0 0 340 40" aria-hidden="true">
      <path d="M8 34 C90 22 200 12 330 6 C260 10 200 16 150 26 C220 20 280 18 300 18" fill="none" stroke="var(--red)" stroke-width="4" stroke-linecap="round"/>
    </svg>

    <p class="intro">Nutzen Sie Ihre <strong>Verhinderungspflege</strong> ab dem Pflegegrad 2 bis zum 31.12.2023, sonst verfällt Ihr Anspruch. Denken Sie auch an Ihren <strong>Entlastungsbetrag</strong> ab Pflegegrad 1.</p>

    <div class="photo" role="img" aria-label="Foto einer lachenden Familie mit Großeltern, Eltern und zwei Kindern"></div>

    <svg class="bands" width="566" height="800" viewBox="0 0 566 800" aria-hidden="true">
      <polygon points="0,700 300,676 566,560 566,670 160,712 0,770" fill="var(--red)"/>
      <polygon points="390,668 566,560 566,650" fill="var(--red-light)"/>
      <polygon points="0,770 160,712 566,660 566,800 0,800" fill="var(--dark)"/>
    </svg>
    <p class="footer-url">www.lindaufeld.de</p>
  </section>

  <section class="page page--right">
    <div class="photo photo--faint" role="img" aria-label="Blasses Hintergrundfoto zweier sich haltender Hände"></div>

    <div class="brand"><span class="brand__mark"></span><span class="brand__name">LINDAUFELD</span></div>
    <p class="tagline">Wir sind für Sie da!</p>

    <svg class="ribbon" width="420" height="80" viewBox="0 0 420 80" aria-hidden="true">
      <polygon points="40,8 410,2 400,48 50,58" fill="var(--dark)"/>
      <polygon points="0,30 400,14 408,60 16,76" fill="var(--red)"/>
      <polygon points="14,34 392,20 398,54 26,68" fill="none" stroke="var(--white)" stroke-width="1" stroke-dasharray="5 4"/>
      <text x="206" y="56" text-anchor="middle" fill="var(--white)" font-family="Open Sans, Arial, sans-serif" font-weight="800" font-size="25" letter-spacing="1.5">UNSERE VORTEILE</text>
    </svg>

    <p class="benefits-intro">Als anerkannter und zugelassener Dienstleister für haushaltsnahe Services, können wir unsere Leistungen über den Entlastungsbetrag oder der Verhinderungspflege direkt mit Ihrer Pflegekasse abrechnen!</p>

    <div class="benefit benefit--billing">
      <span class="benefit__icon"><svg width="26" height="30" viewBox="0 0 26 30" aria-hidden="true"><rect x="2" y="2" width="22" height="26" rx="2" fill="none" stroke="#fff" stroke-width="2"/><path d="M7 9h12M7 14h12M7 19h12M7 24h7" stroke="#fff" stroke-width="2"/></svg></span>
      <span>Abrechnung mit allen Pflegekassen möglich</span>
    </div>
    <div class="benefit benefit--amount">
      <span class="benefit__icon"><svg width="30" height="30" viewBox="0 0 30 30" aria-hidden="true"><path d="M11 2h8v6h6v8h-6v6h-8v-6H5V8h6z" fill="#fff"/><path d="M2 26c6-3 12-3 17 0l9-4" fill="none" stroke="#fff" stroke-width="2"/></svg></span>
      <span>Abrechnung über den Entlastungsbetrag von mind. 125 € mtl. ab Pflegegrad 1 möglich</span>
    </div>
    <div class="benefit benefit--application">
      <span class="benefit__icon"><svg width="30" height="30" viewBox="0 0 30 30" aria-hidden="true"><rect x="3" y="3" width="20" height="24" rx="2" fill="none" stroke="#fff" stroke-width="2"/><path d="M7 9h5M7 15h12M7 20h8" stroke="#fff" stroke-width="2"/><path d="M18 24l9-11" stroke="#fff" stroke-width="3" stroke-linecap="round"/></svg></span>
      <span>Hilfe bei der Antragsstellung</span>
    </div>
    <div class="benefit benefit--respite">
      <span class="benefit__icon"><svg width="32" height="30" viewBox="0 0 32 30" aria-hidden="true"><path d="M16 16c-6-4-8-7-8-9a4 4 0 0 1 8-1 4 4 0 0 1 8 1c0 2-2 5-8 9z" fill="#fff"/><path d="M3 14l6 10h6M29 14l-6 10h-6" fill="none" stroke="#fff" stroke-width="2.5" stroke-linejoin="round"/></svg></span>
      <span>Auch über die Verhinderungspflege</span>
    </div>

    <p class="cta">Buchen Sie gleich einen Termin:</p>
    <div class="phone">
      <span class="phone__icon"><svg width="22" height="22" viewBox="0 0 24 24" aria-hidden="true"><path d="M6 2l4 4-2 3c1 3 4 6 7 7l3-2 4 4-3 4C10 22 2 14 2 5z" fill="var(--red)"/></svg></span>
      <span class="phone__number">0711 28 63 90 57</span>
    </div>

    <svg class="bands" width="566" height="800" viewBox="0 0 566 800" aria-hidden="true">
      <polygon points="0,626 190,690 390,610 566,596 566,676 0,712" fill="var(--red)"/>
      <polygon points="0,626 190,690 60,700 0,712" fill="var(--red-deep)"/>
      <polygon points="0,712 250,690 566,640 566,800 0,800" fill="var(--dark)"/>
    </svg>
    <p class="footer-url">www.lindaufeld.de</p>
  </section>

</main>
</body>
</html>
```